Business Card Design

We are a contracting firm, 95% of my work is interior renovations.... but also don't want to preclude the idea of doing exterior work if it arises. I Need a business card that says I am the ultimate professional. There is a per-determined notion that all contractors are shady, unreliable, etc. Being that most of my work is in Manhattan, I would like to give the impression of fresh, modern, sleek, design/build firm.

Target Market(s)

young couples 25-40

Industry/Entity Type

Business

Contact Information for Business Card

PeterHollowayBuilders LLC
27 North Birchwood Lane
Elm Hollow NY 11000
718-555-0193
646-555-0148- cell
www.phbrx.com
ph@phbrx.com
Peter Holloway

Requirements
Should not have
• do not want to give the impression of a "bargain basement store"

```html
<!DOCTYPE html>
<html lang="en">
<head>
<meta charset="utf-8">
<title>Peter Holloway Builders – Business Card</title>
<link rel="stylesheet" href="https://fonts.googleapis.com/css2?family=Cormorant+Garamond:wght@500&family=Arimo:wght@400&display=swap">
<style>
  :root {
    --canvas: #6f6f70;
    --charcoal: #38383a;
    --charcoal-deep: #2e2e30;
    --navy: #2c4763;
    --blue: #2b7fc3;
    --paper: #ffffff;
    --mist: #e9ecee;
    --ink: #1f3550;
    --grey-text: #5a5c60;
  }
  * { margin: 0; padding: 0; box-sizing: border-box; }
  html, body { width: 1135px; height: 1200px; overflow: hidden; }
  body {
    background: var(--canvas);
    position: relative;
    font-family: "Arimo", Arial, sans-serif;
  }
  .card {
    position: absolute;
    left: 217px;
    width: 700px;
    height: 400px;
    overflow: hidden;
    box-shadow: 0 6px 18px rgba(0,0,0,.35);
  }
  .card svg.card-shapes { position: absolute; inset: 0; }
  .card-front { top: 40px; background: var(--charcoal); }
  .card-back { top: 465px; background: var(--paper); }

  .wordmark {
    position: absolute;
    font-family: "Cormorant Garamond", Georgia, serif;
    font-weight: 500;
    color: var(--paper);
    text-align: center;
    text-transform: uppercase;
    line-height: 1.05;
  }
  .card-front .wordmark {
    left: 0; right: 0; top: 85px;
    font-size: 50px;
    letter-spacing: 4px;
  }
  .wordmark .trade { display: block; font-size: 0.62em; letter-spacing: 0.6em; margin-top: 8px; }

  .website {
    position: absolute;
    left: 0; right: 0; top: 288px;
    text-align: center;
    font-size: 20px;
    letter-spacing: 6px;
    color: var(--charcoal-deep);
  }

  .owner-name {
    position: absolute;
    left: 0; right: 0; top: 52px;
    text-align: center;
    font-family: "Cormorant Garamond", Georgia, serif;
    font-weight: 500;
    font-size: 44px;
    letter-spacing: 4px;
    color: var(--ink);
    text-transform: uppercase;
  }
  .contact {
    position: absolute;
    top: 150px;
    font-size: 15px;
    letter-spacing: 2.5px;
    line-height: 1.45;
    color: var(--grey-text);
  }
  .contact-address { left: 46px; }
  .contact-lines { right: 40px; text-align: right; }
  .contact-row { display: flex; align-items: center; gap: 8px; }
  .contact-lines .contact-row { justify-content: flex-end; }
  .icon { width: 14px; height: 14px; flex: none; }

  .logo-banner {
    position: absolute;
    left: 40px; top: 915px;
    width: 1055px; height: 245px;
    background: var(--charcoal);
  }
  .logo-banner .wordmark {
    left: 0; right: 0; top: 58px;
    font-size: 66px;
    letter-spacing: 6px;
  }
</style>
</head>
<body>

  <section class="card card-front" aria-label="Card front">
    <svg class="card-shapes" width="700" height="400" viewBox="0 0 700 400">
      <polygon points="430,0 700,0 700,70" fill="var(--blue)"/>
      <polygon points="560,0 700,0 700,35" fill="var(--navy)"/>
      <polygon points="0,250 700,280 700,345 0,330" fill="var(--mist)"/>
      <polygon points="0,262 700,292 700,345 0,318" fill="var(--paper)"/>
      <polygon points="0,372 700,382 700,400 0,400" fill="var(--navy)"/>
      <polygon points="0,388 700,394 700,400 0,400" fill="var(--blue)"/>
    </svg>
    <div class="wordmark">Peter Holloway<span class="trade">Builders</span></div>
    <div class="website">www.phbrx.com</div>
  </section>

  <section class="card card-back" aria-label="Card back">
    <svg class="card-shapes" width="700" height="400" viewBox="0 0 700 400">
      <polygon points="0,0 700,0 700,30 0,18" fill="var(--charcoal)"/>
      <polygon points="0,18 700,30 700,36 0,24" fill="var(--navy)"/>
      <polygon points="120,60 620,55 600,125 160,120" fill="var(--mist)"/>
      <polygon points="0,300 700,285 700,400 0,400" fill="var(--charcoal)"/>
      <polygon points="0,350 700,355 700,362 0,358" fill="var(--navy)"/>
      <polygon points="0,380 700,386 700,392 0,388" fill="var(--blue)"/>
    </svg>
    <div class="owner-name">Peter Holloway</div>

    <div class="contact contact-address">
      <div class="contact-row">
        <svg class="icon" viewBox="0 0 14 14" aria-hidden="true"><path d="M7 1a4 4 0 0 1 4 4c0 3-4 8-4 8S3 8 3 5a4 4 0 0 1 4-4z" fill="none" stroke="var(--blue)" stroke-width="1.6"/><circle cx="7" cy="5" r="1.4" fill="var(--blue)"/></svg>
        <span>PeterHollowayBuilders LLC</span>
      </div>
      <div>27 North Birchwood Lane</div>
      <div>Elm Hollow NY 11000</div>
    </div>

    <div class="contact contact-lines">
      <div class="contact-row"><span>718 555 0193</span>
        <svg class="icon" viewBox="0 0 14 14" aria-hidden="true"><rect width="14" height="14" rx="2" fill="var(--blue)"/><path d="M4.3 3.2l1.5 1.8-.8 1a5 5 0 0 0 2.9 2.9l1-.8 1.8 1.5-1 1.2C6.6 10.6 3.4 7.4 3.2 4.3z" fill="var(--paper)"/></svg>
      </div>
      <div class="contact-row"><span>646 555 0148</span><span class="icon"></span></div>
      <div class="contact-row"><span>ph@phbrx.com</span>
        <svg class="icon" viewBox="0 0 14 14" aria-hidden="true"><circle cx="7" cy="7" r="7" fill="var(--blue)"/><rect x="3.5" y="4.5" width="7" height="5" fill="none" stroke="var(--paper)" stroke-width="1"/><path d="M3.5 4.5L7 7.3l3.5-2.8" fill="none" stroke="var(--paper)" stroke-width="1"/></svg>
      </div>
    </div>
  </section>

  <section class="logo-banner" aria-label="Wordmark">
    <div class="wordmark">Peter Holloway<span class="trade">Builders</span></div>
  </section>

</body>
</html>
```